Catalog for Varno Gearworks featuring all the model of Pierre Calvet Roof Top Tents

Creative Catalog to hand out to visitors of Outdoor Expos. The Catalog branding will be VARNO Gearworks Featuring
Pierre Calvet Roof Top Tents / Exclusive Dealer
Having two pages each for each of the tent models showing multiple pictures and specifications:
Horizon
Summit
Canopy
Nomad / Nomad XXL
Ranger
Long Trail
and then multiple pages as necessary for accessories, Custom colors, and company information.

Target Market(s)

Adventure Travelers

Font styles to use
Sans Serif

Requirements
Must have
• 5.5" x 8.5" horizontal layout ideally around 20 pages (16 + covers)
Catalog must have the feel, logos and imagery of our VARNO gearworks branding: https://www.facebook.com/VarnoGear/

would want phone number: (513) 762-1938 and website www.Varno.Gear at the bottom of every other page. I would like to have 2 pages for EACH tent model. one page showing an environmental shot of the tent. photos can be found here:
https://www.pierrecalvet.example/en/galleries/
https://www.facebook.com/PierreCalvetOfficial/photos/?ref=page_internal
the 2nd page showing actual product photos description and specifications:
https://www.pierrecalvet.example/en/products/

```html
<!DOCTYPE html>
<html lang="en">
<head>
<meta charset="utf-8">
<title>Varno Gearworks – Pierre Calvet Roof Top Tent Catalog</title>
<link rel="stylesheet" href="https://fonts.googleapis.com/css2?family=Montserrat:wght@200;300;400;600;700;800&display=swap">
<style>
  :root {
    --backdrop: #e4e4e6;
    --slate: #3b4350;
    --slate-deep: #2b313a;
    --paper: #f4f4f4;
    --rule: #d6d6d6;
    --ink: #2c2f35;
    --ink-soft: #5f646d;
    --on-dark: #ffffff;
    --on-dark-soft: #c3c8d0;
    --photo-light: #e9e9e9;
    --photo-mid: #8d8d8d;
    --photo-dark: #3d3d3d;
    --accent: #3fa6d8;
  }
  * { box-sizing: border-box; margin: 0; padding: 0; }
  html, body { width: 1200px; height: 3000px; overflow: hidden; background: var(--backdrop); }
  body { font-family: "Montserrat", sans-serif; color: var(--ink); }

  .catalog { display: flex; flex-direction: column; align-items: center; gap: 155px; padding-top: 150px; }

  /* Front cover */
  .cover { position: relative; width: 1000px; height: 647px; overflow: hidden; background: var(--slate); box-shadow: 0 6px 20px rgba(0,0,0,.18); }
  .cover-shapes { position: absolute; inset: 0; }
  .cover-photo { position: absolute; inset: 0; clip-path: polygon(440px 0, 1000px 0, 1000px 647px, 752px 647px, 622px 290px); background: linear-gradient(200deg, var(--photo-light) 0%, #bdbdbd 30%, var(--photo-mid) 60%, var(--photo-dark) 100%); }
  .brand { position: absolute; left: 96px; top: 120px; display: flex; align-items: center; gap: 12px; color: var(--on-dark); }
  .brand-mark { width: 34px; height: 34px; background: var(--accent); }
  .brand-name { display: block; font-weight: 700; font-size: 28px; letter-spacing: 1px; line-height: 1; }
  .brand-sub { display: block; font-size: 12px; font-weight: 700; letter-spacing: 2px; margin-top: 4px; }
  .cover-headline { position: absolute; left: 96px; top: 240px; color: var(--on-dark); }
  .cover-kicker { font-weight: 200; font-size: 44px; letter-spacing: 1px; line-height: 1; }
  .cover-title { font-weight: 800; font-size: 60px; letter-spacing: 1px; line-height: 1.05; }
  .cover-sub { font-weight: 700; font-size: 27px; letter-spacing: 1px; line-height: 1.1; }
  .cover-rule { width: 360px; height: 2px; background: var(--on-dark-soft); margin-top: 18px; }
  .cover-web { position: absolute; left: 300px; bottom: 60px; font-size: 20px; font-weight: 400; color: var(--on-dark); letter-spacing: 1px; }

  /* Spreads */
  .spread { position: relative; width: 1100px; height: 356px; background: var(--paper); overflow: hidden; box-shadow: 0 6px 20px rgba(0,0,0,.18); }
  .spread-shapes { position: absolute; inset: 0; }
  .gutter { position: absolute; left: 530px; top: 0; width: 40px; height: 100%; background: linear-gradient(90deg, transparent, rgba(0,0,0,.16) 50%, transparent); pointer-events: none; }

  .cover-small { position: absolute; left: 550px; top: 0; width: 1000px; height: 647px; transform: scale(.55); transform-origin: 0 0; box-shadow: none; }
  .back-cover { position: absolute; left: 0; top: 0; width: 550px; height: 356px; background: linear-gradient(135deg, var(--slate) 0%, var(--slate-deep) 100%); }
  .back-contact { position: absolute; left: 36px; bottom: 30px; display: flex; align-items: flex-end; gap: 24px; color: var(--on-dark); }
  .back-contact .brand { position: static; }
  .back-contact .brand-mark { width: 20px; height: 20px; }
  .back-contact .brand-name { font-size: 16px; }
  .back-contact .brand-sub { font-size: 7px; }
  .contact-list { list-style: none; font-size: 11px; line-height: 1.8; }
  .contact-list li { display: flex; align-items: center; gap: 8px; }
  .contact-list svg { width: 11px; height: 11px; }

  .thumbs { position: absolute; display: flex; flex-direction: column; gap: 8px; }
  .thumb { height: 106px; border-bottom: 1px solid var(--rule); display: flex; align-items: center; justify-content: center; }
  .thumb span { display: block; width: 62%; height: 72%; border-radius: 6px; background: linear-gradient(160deg, #d8d8d8, #6f6f6f 70%, #3a3a3a); }
  .thumbs.on-dark .thumb { border-color: rgba(255,255,255,.25); }
  .thumbs.on-dark .thumb span { background: linear-gradient(160deg, #9a9a9a, #4a4a4a 70%, #222); }

  .model { position: absolute; top: 40px; width: 210px; }
  .model-title { font-size: 12px; font-weight: 700; letter-spacing: .5px; margin-bottom: 14px; white-space: nowrap; }
  .model-body { font-size: 8px; line-height: 1.7; font-weight: 400; }
  .model-body p + p { margin-top: 8px; }
  .model.on-dark { color: var(--on-dark); }
  .model.on-dark .model-body { color: var(--on-dark-soft); }
  .model.on-light .model-title { color: var(--ink); }
  .model.on-light .model-body { color: var(--ink-soft); }

  .foot { position: absolute; bottom: 14px; font-size: 8px; font-weight: 700; display: flex; align-items: center; gap: 5px; white-space: nowrap; }
  .foot svg { width: 8px; height: 8px; }
  .foot.light { color: var(--on-dark); }
  .foot.dark { color: var(--ink); }
</style>
</head>
<body>
<main class="catalog">

  <!-- Front cover -->
  <section class="cover">
    <div class="cover-photo" role="img" aria-label="Black and white photo of hikers walking over a grassy ridge"></div>
    <svg class="cover-shapes" viewBox="0 0 1000 647" aria-hidden="true">
      <polyline points="440,0 622,290 752,647" fill="none" stroke="#ffffff" stroke-width="14"/>
      <line x1="640" y1="300" x2="1000" y2="270" stroke="#ffffff" stroke-width="10"/>
    </svg>
    <div class="brand"><span class="brand-mark"></span><div><span class="brand-name">VARNO</span><span class="brand-sub">GEARWORKS</span></div></div>
    <div class="cover-headline">
      <p class="cover-kicker">OWN THE</p>
      <p class="cover-title">OUTDOORS</p>
      <p class="cover-sub">EXCLUSIVE DEALER</p>
      <div class="cover-rule"></div>
    </div>
    <p class="cover-web">www.Varno.Gear</p>
  </section>

  <!-- Back and front cover -->
  <section class="spread">
    <div class="back-cover">
      <div class="back-contact">
        <div class="brand"><span class="brand-mark"></span><div><span class="brand-name">VARNO</span><span class="brand-sub">GEARWORKS</span></div></div>
        <ul class="contact-list">
          <li><svg viewBox="0 0 12 12"><path d="M3 1l2 2-1 1.5a6 6 0 0 0 3.5 3.5L9 7l2 2-1.5 2A9 9 0 0 1 1 2.5z" fill="none" stroke="#fff" stroke-width="1"/></svg>+1 (513) 762-1938</li>
          <li><svg viewBox="0 0 12 12"><rect x="1" y="2.5" width="10" height="7" fill="none" stroke="#fff"/><path d="M1 2.5l5 4 5-4" fill="none" stroke="#fff"/></svg>info@varno.gear</li>
          <li><svg viewBox="0 0 12 12"><circle cx="6" cy="6" r="5" fill="#fff"/></svg>www.Varno.Gear</li>
        </ul>
      </div>
    </div>
    <div class="cover cover-small">
      <div class="cover-photo" role="img" aria-label="Black and white photo of hikers walking over a grassy ridge"></div>
      <svg class="cover-shapes" viewBox="0 0 1000 647" aria-hidden="true">
        <polyline points="440,0 622,290 752,647" fill="none" stroke="#ffffff" stroke-width="14"/>
        <line x1="640" y1="300" x2="1000" y2="270" stroke="#ffffff" stroke-width="10"/>
      </svg>
      <div class="brand"><span class="brand-mark"></span><div><span class="brand-name">VARNO</span><span class="brand-sub">GEARWORKS</span></div></div>
      <div class="cover-headline">
        <p class="cover-kicker">OWN THE</p>
        <p class="cover-title">OUTDOORS</p>
        <p class="cover-sub">EXCLUSIVE DEALER</p>
        <div class="cover-rule"></div>
      </div>
      <p class="cover-web">www.Varno.Gear</p>
    </div>
    <div class="gutter"></div>
  </section>

  <!-- Summit / Horizon -->
  <section class="spread">
    <svg class="spread-shapes" viewBox="0 0 1100 356" aria-hidden="true">
      <polygon points="280,0 860,0 830,356 250,356" fill="var(--slate)"/>
    </svg>
    <div class="thumbs" style="left:10px;top:10px;width:220px;">
      <div class="thumb" role="img" aria-label="Summit tent open, angled view"><span></span></div>
      <div class="thumb" role="img" aria-label="Summit tent open, front view"><span></span></div>
      <div class="thumb" role="img" aria-label="Summit tent shell closed, side view"><span></span></div>
    </div>
    <article class="model on-dark" style="left:300px;">
      <h2 class="model-title">ROOFLINE SUMMIT</h2>
      <div class="model-body">
        <p>A Pierre Calvet hard shell made for steep tracks and high passes. Gas struts raise the roof in seconds.</p>
        <p>Sleeps two on a dense foam mattress. Weight 60 kg, closed height 28 cm.</p>
        <p>Offered in standard and XL sizes.</p>
      </div>
    </article>
    <article class="model on-dark" style="left:585px;">
      <h2 class="model-title">ROOFLINE HORIZON</h2>
      <div class="model-body">
        <p>The Pierre Calvet classic: a wedge roof that opens in one move and stays quiet in strong wind.</p>
        <p>Three wide mesh windows, inner lights and a deep mattress. Weight 55 kg.</p>
        <p>Offered in standard and XL sizes.</p>
      </div>
    </article>
    <div class="thumbs" style="left:870px;top:10px;width:220px;">
      <div class="thumb" role="img" aria-label="Horizon tent open, angled view"><span></span></div>
      <div class="thumb" role="img" aria-label="Horizon tent open, rear view"><span></span></div>
      <div class="thumb" role="img" aria-label="Horizon tent open, side view"><span></span></div>
    </div>
    <p class="foot dark" style="left:20px;"><svg viewBox="0 0 12 12"><path d="M3 1l2 2-1 1.5a6 6 0 0 0 3.5 3.5L9 7l2 2-1.5 2A9 9 0 0 1 1 2.5z" fill="currentColor"/></svg>+1 (513) 762-1938</p>
    <p class="foot light" style="left:420px;"><svg viewBox="0 0 12 12"><circle cx="6" cy="6" r="5" fill="currentColor"/></svg>www.Varno.Gear</p>
    <p class="foot light" style="left:590px;"><svg viewBox="0 0 12 12"><circle cx="6" cy="6" r="5" fill="currentColor"/></svg>www.Varno.Gear</p>
    <p class="foot dark" style="right:20px;"><svg viewBox="0 0 12 12"><path d="M3 1l2 2-1 1.5a6 6 0 0 0 3.5 3.5L9 7l2 2-1.5 2A9 9 0 0 1 1 2.5z" fill="currentColor"/></svg>+1 (513) 762-1938</p>
    <div class="gutter"></div>
  </section>

  <!-- Nomad / Canopy -->
  <section class="spread">
    <svg class="spread-shapes" viewBox="0 0 1100 356" aria-hidden="true">
      <polygon points="0,0 270,0 240,356 0,356" fill="var(--slate-deep)"/>
      <polygon points="870,0 1100,0 1100,356 840,356" fill="var(--slate)"/>
    </svg>
    <div class="thumbs on-dark" style="left:10px;top:10px;width:220px;">
      <div class="thumb" role="img" aria-label="Nomad tent open, angled view"><span></span></div>
      <div class="thumb" role="img" aria-label="Nomad XXL tent closed, side view"><span></span></div>
      <div class="thumb" role="img" aria-label="Nomad tent shell from above"><span></span></div>
    </div>
    <article class="model on-light" style="left:295px;">
      <h2 class="model-title">ROOFLINE NOMAD</h2>
      <div class="model-body">
        <p>The roomiest Pierre Calvet shell, with a full-length roof that lifts straight up on four struts.</p>
        <p>Sleeps up to four in the XXL. Weight 75 kg, floor 230 x 160 cm.</p>
        <p>Nomad and Nomad XXL versions.</p>
      </div>
    </article>
    <article class="model on-light" style="left:590px;">
      <h2 class="model-title">ROOFLINE CANOPY</h2>
      <div class="model-body">
        <p>A tall, bright cabin with panoramic windows on every side and a fast vertical opening.</p>
        <p>Sleeps two adults and a child. Weight 68 kg, inner height 120 cm.</p>
        <p>Offered in standard and XL sizes.</p>
      </div>
    </article>
    <div class="thumbs on-dark" style="left:875px;top:10px;width:215px;">
      <div class="thumb" role="img" aria-label="Canopy tent open, front view"><span></span></div>
      <div class="thumb" role="img" aria-label="Canopy tent open, angled view"><span></span></div>
      <div class="thumb" role="img" aria-label="Canopy tent closed, side view"><span></span></div>
    </div>
    <p class="foot light" style="left:20px;"><svg viewBox="0 0 12 12"><path d="M3 1l2 2-1 1.5a6 6 0 0 0 3.5 3.5L9 7l2 2-1.5 2A9 9 0 0 1 1 2.5z" fill="currentColor"/></svg>+1 (513) 762-1938</p>
    <p class="foot dark" style="left:420px;"><svg viewBox="0 0 12 12"><circle cx="6" cy="6" r="5" fill="currentColor"/></svg>www.Varno.Gear</p>
    <p class="foot dark" style="left:590px;"><svg viewBox="0 0 12 12"><circle cx="6" cy="6" r="5" fill="currentColor"/></svg>www.Varno.Gear</p>
    <p class="foot light" style="right:20px;"><svg viewBox="0 0 12 12"><path d="M3 1l2 2-1 1.5a6 6 0 0 0 3.5 3.5L9 7l2 2-1.5 2A9 9 0 0 1 1 2.5z" fill="currentColor"/></svg>+1 (513) 762-1938</p>
    <div class="gutter"></div>
  </section>

  <!-- Long Trail / Ranger -->
  <section class="spread">
    <svg class="spread-shapes" viewBox="0 0 1100 356" aria-hidden="true">
      <polygon points="320,0 820,0 880,178 820,356 320,356 260,178" fill="var(--slate)"/>
    </svg>
    <div class="thumbs" style="left:10px;top:10px;width:220px;">
      <div class="thumb" role="img" aria-label="Long Trail tent open, angled view"><span></span></div>
      <div class="thumb" role="img" aria-label="Long Trail tent open, side view"><span></span></div>
      <div class="thumb" role="img" aria-label="Long Trail tent closed, side view"><span></span></div>
    </div>
    <article class="model on-dark" style="left:330px;">
      <h2 class="model-title">ROOFLINE LONG TRAIL</h2>
      <div class="model-body">
        <p>Built for long overland routes, with storage inside the shell and a hard floor that doubles as a roof rack.</p>
        <p>Sleeps three. Weight 72 kg, closed height 30 cm.</p>
        <p>Offered in standard and XL sizes.</p>
      </div>
    </article>
    <article class="model on-dark" style="left:590px;">
      <h2 class="model-title">ROOFLINE RANGER</h2>
      <div class="model-body">
        <p>A low, light shell for daily driving that turns into a full camp in under a minute.</p>
        <p>Sleeps two. Weight 52 kg, closed height 26 cm.</p>
        <p>Offered in standard and XL sizes.</p>
      </div>
    </article>
    <div class="thumbs" style="left:880px;top:10px;width:210px;">
      <div class="thumb" role="img" aria-label="Ranger tent open, front view"><span></span></div>
      <div class="thumb" role="img" aria-label="Ranger tent open, angled view"><span></span></div>
      <div class="thumb" role="img" aria-label="Ranger tent closed, side view"><span></span></div>
    </div>
    <p class="foot dark" style="left:20px;"><svg viewBox="0 0 12 12"><path d="M3 1l2 2-1 1.5a6 6 0 0 0 3.5 3.5L9 7l2 2-1.5 2A9 9 0 0 1 1 2.5z" fill="currentColor"/></svg>+1 (513) 762-1938</p>
    <p class="foot light" style="left:420px;"><svg viewBox="0 0 12 12"><circle cx="6" cy="6" r="5" fill="currentColor"/></svg>www.Varno.Gear</p>
    <p class="foot light" style="left:590px;"><svg viewBox="0 0 12 12"><circle cx="6" cy="6" r="5" fill="currentColor"/></svg>www.Varno.Gear</p>
    <p class="foot dark" style="right:20px;"><svg viewBox="0 0 12 12"><path d="M3 1l2 2-1 1.5a6 6 0 0 0 3.5 3.5L9 7l2 2-1.5 2A9 9 0 0 1 1 2.5z" fill="currentColor"/></svg>+1 (513) 762-1938</p>
    <div class="gutter"></div>
  </section>

</main>
</body>
</html>
```